Psychologist Banner Ads for Remarketing & plimora

Brand awareness campaign for tallowbrook.com.au

// Ad Formats //
Static JPEG
Max 45KB in file size
All ads must have a border

// Ad Sizes //
Static: (for Brixel Display network) 300×250, 160×600, 728×90
Static: (for Plimora, no more than 25% text): 600×315, 1200 x 627

Please use logo, image and "maximise your wellbeing" from the website home page.

```html
<!DOCTYPE html>
<html lang="en">
<head>
<meta charset="utf-8">
<title>Tallowbrook Psychology – Display Banner Set</title>
<link rel="stylesheet" href="https://fonts.googleapis.com/css2?family=Arimo:wght@400;700&family=Ultra&display=swap">
<style>
  :root {
    --stage: #ececec;
    --frame: #111111;
    --panel-cyan: #6ccbe0;
    --headline-white: #ffffff;
    --navy: #1b4597;
    --sky-light: #f4fbfe;
    --sky-mid: #cdeaf6;
    --skin-warm: #d9b9a4;
  }

  * { box-sizing: border-box; margin: 0; padding: 0; }

  html, body {
    width: 1200px;
    height: 900px;
    overflow: hidden;
    background: var(--stage);
    font-family: "Arimo", Arial, sans-serif;
  }

  .canvas {
    position: relative;
    width: 1200px;
    height: 900px;
  }

  .banner {
    position: absolute;
    overflow: hidden;
    border: 3px solid var(--frame);
    background: var(--sky-light);
  }

  .banner__photo {
    position: absolute;
    inset: 0;
    background: linear-gradient(160deg, var(--sky-light) 0%, var(--sky-mid) 55%, var(--skin-warm) 130%);
  }

  .banner__panel {
    position: absolute;
    inset: 0;
    width: 100%;
    height: 100%;
  }

  .banner__panel polygon { fill: var(--panel-cyan); }

  .headline {
    position: absolute;
    font-family: "Ultra", "Rockwell", serif;
    color: var(--headline-white);
    letter-spacing: 0.5px;
    line-height: 1;
    text-align: center;
    white-space: nowrap;
  }

  .subline {
    position: absolute;
    color: var(--navy);
    line-height: 1.1;
    text-align: center;
    white-space: nowrap;
  }

  .brand {
    position: absolute;
    color: var(--navy);
    font-weight: 400;
    line-height: 1.05;
    text-align: center;
  }

  /* 728 x 90 leaderboard */
  .banner--leaderboard { left: 178px; top: 45px; width: 851px; height: 103px; }
  .banner--leaderboard .banner__photo { background: linear-gradient(90deg, var(--sky-mid) 0%, var(--sky-light) 40%, var(--skin-warm) 120%); }
  .banner--leaderboard .headline { left: 352px; width: 300px; top: 18px; font-size: 34px; }
  .banner--leaderboard .subline { left: 352px; width: 300px; top: 56px; font-size: 23px; }
  .banner--leaderboard .brand { left: 690px; width: 150px; top: 22px; font-size: 22px; }

  /* 300 x 250 medium rectangle */
  .banner--rectangle { left: 341px; top: 332px; width: 351px; height: 291px; }
  .banner--rectangle .brand { left: 12px; width: 150px; top: 102px; font-size: 21px; }
  .banner--rectangle .headline { left: 0; width: 310px; top: 206px; font-size: 32px; }
  .banner--rectangle .subline { left: 0; width: 310px; top: 240px; font-size: 23px; }

  /* 160 x 600 skyscraper */
  .banner--skyscraper { left: 844px; top: 170px; width: 185px; height: 700px; }
  .banner--skyscraper .brand { left: 0; width: 179px; top: 348px; font-size: 22px; }
  .banner--skyscraper .headline { left: 0; width: 179px; top: 468px; font-size: 24px; }
  .banner--skyscraper .subline { left: 0; width: 179px; top: 508px; font-size: 36px; line-height: 1.2; }
</style>
</head>
<body>
<main class="canvas">

  <section class="banner banner--leaderboard" aria-label="728 by 90 leaderboard banner">
    <div class="banner__photo" role="img" aria-label="Photo of a smiling woman raising her arms against a pale blue sky"></div>
    <svg class="banner__panel" viewBox="0 0 845 97" preserveAspectRatio="none" aria-hidden="true">
      <polygon points="346,0 845,0 845,97 300,97"/>
    </svg>
    <p class="headline">MAXIMISE</p>
    <p class="subline">Your Wellbeing</p>
    <p class="brand">Tallowbrook<br>Psychology</p>
  </section>

  <section class="banner banner--rectangle" aria-label="300 by 250 rectangle banner">
    <div class="banner__photo" role="img" aria-label="Photo of a smiling woman raising her arms against a pale blue sky"></div>
    <svg class="banner__panel" viewBox="0 0 345 285" preserveAspectRatio="none" aria-hidden="true">
      <polygon points="0,106 345,232 345,285 0,285"/>
    </svg>
    <p class="brand">Tallowbrook<br>Psychology</p>
    <p class="headline">MAXIMISE</p>
    <p class="subline">Your Wellbeing</p>
  </section>

  <section class="banner banner--skyscraper" aria-label="160 by 600 skyscraper banner">
    <div class="banner__photo" role="img" aria-label="Photo of a smiling woman raising her arms against a pale blue sky"></div>
    <svg class="banner__panel" viewBox="0 0 179 694" preserveAspectRatio="none" aria-hidden="true">
      <polygon points="0,267 179,332 179,694 0,694"/>
    </svg>
    <p class="brand">Tallowbrook<br>Psychology</p>
    <p class="headline">MAXIMISE</p>
    <p class="subline">Your<br>Wellbeing</p>
  </section>

</main>
</body>
</html>
```